Home Water Filter Product Labels

We are looking for label design for a home water filter system. Attached files include examples of similar systems with sample labels. The file attached as Kel Mira logo is our brand/logo and should be incorporated into each label and the text file explains what text should be included on each label of the system. There are a total of 6 labels on the system, 3 of which should be identical except for text and color.
Design Requirements:
-The attached logo should be used on the labels.
-The colors in the label should be used throughout the labels
-Label 1,2,3 should be the same design but different colors like the examples
-Labels Should not be copies of the examples but similar layout with different design
-Design needs to represent a clean feeling but can also be slightly industrial
-The finished files need to have the text editable in case we need to change wording.

Industry/Entity Type

Product

Font styles to use
Sans Serif

Colors

Designer to choose colors to be used in the design.

Requirements
Must have
• ***ALL DESIGN DIMENSIONS ARE IN INCHES**
• Labels 1-3:
• - Same design different colors for each label
• label 6:
• - Must incorporate our logo but include "Vantage Line"

```html
<!DOCTYPE html>
<html lang="en">
<head>
<meta charset="utf-8">
<title>Kel Mira – Pre Carbon Filter Label</title>
<link href="https://fonts.googleapis.com/css2?family=Archivo:ital,wdth,wght@0,62..125,400;0,62..125,700;0,62..125,800;1,62..125,800&display=swap" rel="stylesheet">
<style>
  :root {
    --brand-green: #5b9b32;
    --deep-green: #248836;
    --ink: #2e2e2e;
    --muted-grey: #c8c8c8;
    --band-grey: #f0f0f0;
    --white: #ffffff;
  }
  * { margin: 0; padding: 0; box-sizing: border-box; }
  html, body { width: 1200px; height: 2182px; overflow: hidden; background: var(--white); }
  body { font-family: "Archivo", Arial, sans-serif; font-stretch: 100%; color: var(--ink); }
  .label { position: relative; width: 1200px; height: 2182px; overflow: hidden; background: var(--white); }

  .brand { position: absolute; left: 77px; top: 90px; height: 170px; display: flex; align-items: center; gap: 30px; }
  .brand-dot { width: 70px; height: 70px; border-radius: 50%; background: var(--brand-green); }
  .brand-name { font-size: 136px; font-weight: 800; font-stretch: 112%; color: var(--brand-green); letter-spacing: 2px; line-height: 1; }

  .stage-band { position: absolute; left: 844px; top: 353px; width: 356px; height: 188px;
    background: linear-gradient(90deg, var(--white) 0%, var(--band-grey) 100%); }
  .stage-number { position: absolute; left: 840px; top: 318px; font-size: 226px; font-weight: 800; font-style: italic;
    font-stretch: 125%; color: var(--muted-grey); line-height: 1; }

  .product-title { position: absolute; left: 77px; top: 484px; font-size: 58px; font-weight: 800; font-stretch: 125%;
    color: var(--brand-green); letter-spacing: 0.5px; line-height: 1; }

  .tab { position: absolute; left: 0; height: 52px; background: var(--brand-green); color: var(--white);
    font-size: 31px; font-weight: 700; display: flex; align-items: center; padding-left: 77px;
    border-radius: 0 26px 26px 0; }
  .tab-series { top: 610px; width: 349px; }
  .tab-requirements { top: 864px; width: 566px; }

  .description { position: absolute; left: 77px; top: 697px; width: 1010px; font-size: 33px; line-height: 44px; }

  .spec-heading { position: absolute; left: 77px; font-size: 35px; font-weight: 400; color: var(--brand-green); }
  .spec-heading.temp { top: 955px; }
  .spec-heading.press { top: 1148px; }

  .spec-table { position: absolute; left: 77px; font-size: 32px; border-collapse: collapse; }
  .spec-table td { padding: 0; height: 45px; vertical-align: middle; }
  .spec-table td.label-cell { width: 217px; }
  .spec-table td.metric { width: 219px; font-weight: 700; }
  .spec-table td.imperial { font-weight: 700; }
  .spec-table.temp { top: 1014px; }
  .spec-table.press { top: 1207px; }

  .replacement-note { position: absolute; left: 0; top: 1337px; width: 1200px; text-align: center; font-size: 27px; line-height: 37px; }

  .warning-rule { position: absolute; left: 0; top: 1490px; width: 1200px; height: 3px; background: var(--brand-green); }
  .warning-pill { position: absolute; left: 426px; top: 1466px; width: 348px; height: 52px; background: var(--white);
    border: 3px solid var(--brand-green); border-radius: 26px; color: var(--brand-green); font-size: 35px;
    display: flex; align-items: center; justify-content: center; letter-spacing: 1px; }
  .warning-text { position: absolute; left: 80px; top: 1550px; width: 1040px; text-align: center; font-size: 34px; line-height: 44px; }

  .footer-band { position: absolute; left: 0; top: 1700px; width: 1200px; height: 482px;
    background: linear-gradient(180deg, rgba(91,155,50,0) 0%, var(--brand-green) 45%, var(--deep-green) 100%); }
</style>
</head>
<body>
<main class="label">
  <header class="brand">
    <span class="brand-dot"></span>
    <span class="brand-name">KEL MIRA</span>
  </header>

  <div class="stage-band"></div>
  <div class="stage-number">2</div>
  <h1 class="product-title">PRE CARBON FILTER</h1>

  <div class="tab tab-series">Vantage Line</div>
  <p class="description">This Filter absorbs organic contaminants such as chlorine, pesticides, herbicides and bad taste.</p>

  <div class="tab tab-requirements">Operating Requirements</div>

  <h2 class="spec-heading temp">TEMPERATURE</h2>
  <table class="spec-table temp">
    <tr><td class="label-cell">Min</td><td class="metric">4°C</td><td class="imperial">49°F</td></tr>
    <tr><td class="label-cell">Max</td><td class="metric">52°C</td><td class="imperial">125°F</td></tr>
  </table>

  <h2 class="spec-heading press">PRESSURE</h2>
  <table class="spec-table press">
    <tr><td class="label-cell">Min</td><td class="metric">35PSI</td><td class="imperial">241KPA</td></tr>
    <tr><td class="label-cell">Max</td><td class="metric">80PSI</td><td class="imperial">551KPA</td></tr>
  </table>

  <p class="replacement-note">Manufacturers recommendation is to replace every 6-9 Months<br>depending on incomming water quality.</p>

  <div class="warning-rule"></div>
  <div class="warning-pill">WARNING</div>
  <p class="warning-text">When intended use is for drinking water make sure water is microbiologically safe or adequate disinfection is performed before or after system.</p>

  <div class="footer-band" role="img" aria-label="Decorative green wave graphic along the bottom of the label"></div>
</main>
</body>
</html>
```